KESTREL Communications Business Card- Belsa

Kestrel Integrated Communications is Corporate communications agency with more than 20 years of experience. We become part of the manegement team of our clients in other to improve their outcomes and grow the possitioning of their brand.
We are in Puerto Rico, latin caribbean island
Name: Maribelsa (Belsa) Ocampo
787-555-0148
bocampo@kestrelwing.example

Target Market(s)

finance and pharmaceutical companies

Industry/Entity Type

Business

Contact Information for Business Card

modern, edgy colorful and playfull like our logo

Requirements
Must have
• company logo
• name
• tel
• email

```html
<!DOCTYPE html>
<html lang="en">
<head>
<meta charset="utf-8">
<title>Kestrel Integrated Communications – Business Card</title>
<link rel="stylesheet" href="https://fonts.googleapis.com/css2?family=Montserrat:wght@600;700&family=Quicksand:wght@400&display=swap">
<style>
  :root {
    --page: #ece9e4;
    --paper: #ffffff;
    --orange: #e9612c;
    --charcoal: #3d3a39;
    --brand-brown: #4a4236;
    --light-text: #e4e1de;
  }
  * { margin: 0; padding: 0; box-sizing: border-box; }
  html, body {
    width: 1200px;
    height: 800px;
    overflow: hidden;
    background: var(--page);
  }
  .canvas {
    position: relative;
    width: 1200px;
    height: 800px;
  }
  .card {
    position: absolute;
    left: 350px;
    width: 500px;
    height: 287px;
    overflow: hidden;
    box-shadow: 0 2px 6px rgba(0, 0, 0, 0.18);
  }
  .card--front { top: 85px; }
  .card--back { top: 422px; }
  .card__art {
    position: absolute;
    inset: 0;
    width: 100%;
    height: 100%;
  }
  .art-orange { fill: var(--orange); }
  .art-paper { fill: var(--paper); }
  .art-charcoal { fill: var(--charcoal); }
  .brand-name {
    position: absolute;
    left: 58px;
    top: 108px;
    font-family: "Montserrat", sans-serif;
    font-weight: 700;
    font-size: 32px;
    letter-spacing: 2px;
    color: var(--brand-brown);
  }
  .holder-name {
    position: absolute;
    left: 302px;
    top: 38px;
    font-family: "Montserrat", sans-serif;
    font-weight: 700;
    font-size: 15px;
    letter-spacing: 0.3px;
    color: var(--charcoal);
  }
  .holder-name__last { color: var(--paper); }
  .contact {
    position: absolute;
    right: 48px;
    top: 190px;
    list-style: none;
    font-family: "Quicksand", sans-serif;
    font-size: 13.5px;
    color: var(--light-text);
  }
  .contact__item {
    display: flex;
    justify-content: flex-end;
    align-items: center;
    gap: 8px;
    height: 20px;
  }
  .contact__icon { width: 16px; height: 16px; }
  .icon-ring { fill: none; stroke: var(--light-text); stroke-width: 1.2; }
  .icon-glyph { fill: var(--light-text); }
</style>
</head>
<body>
<main class="canvas">

  <section class="card card--front" aria-label="Card front">
    <svg class="card__art" viewBox="0 0 500 287" aria-hidden="true">
      <rect class="art-orange" width="500" height="287"/>
      <path class="art-paper" d="M0 0 L165 0 C240 18 300 80 335 150 L335 287 L0 287 Z"/>
      <path class="art-charcoal" d="M0 203 C90 245 210 250 295 185 C365 135 425 122 500 118 L500 287 L0 287 Z"/>
    </svg>
    <div class="brand-name">KESTREL</div>
  </section>

  <section class="card card--back" aria-label="Card back">
    <svg class="card__art" viewBox="0 0 500 287" aria-hidden="true">
      <rect class="art-orange" width="500" height="287"/>
      <path class="art-paper" d="M0 0 L165 0 C240 18 300 80 335 150 L335 287 L0 287 Z"/>
      <path class="art-charcoal" d="M0 203 C90 245 210 250 295 185 C365 135 425 122 500 118 L500 287 L0 287 Z"/>
    </svg>
    <div class="brand-name">KESTREL</div>
    <div class="holder-name">MARIBELSA <span class="holder-name__last">OCAMPO</span></div>
    <ul class="contact">
      <li class="contact__item">
        <span>787-555-0148</span>
        <svg class="contact__icon" viewBox="0 0 16 16" aria-hidden="true">
          <circle class="icon-ring" cx="8" cy="8" r="7"/>
          <path class="icon-glyph" d="M4.5 6.5 Q8 4 11.5 6.5 L11 8 L9.5 7.5 L9.5 6.8 Q8 6.4 6.5 6.8 L6.5 7.5 L5 8 Z M5.5 8.5 H10.5 V11 H5.5 Z"/>
        </svg>
      </li>
      <li class="contact__item">
        <span>bocampo@kestrelwing.example</span>
        <svg class="contact__icon" viewBox="0 0 16 16" aria-hidden="true">
          <circle class="icon-ring" cx="8" cy="8" r="7"/>
          <path class="icon-glyph" d="M4.5 6 L8 3.8 L11.5 6 V11 H4.5 Z M5.3 6.4 L8 8.3 L10.7 6.4 L8 4.7 Z"/>
        </svg>
      </li>
    </ul>
  </section>

</main>
</body>
</html>
```